Plakat-Design für Gemeinschaftspraxis
Briefing
Ausgangssituation
Wir sind eine Gemeinschaftspraxis, die aus Ärzten und Physiotherapeuten besteht. Diese sollen unter einer gemeinsamen Marke präsentiert werden, dem sogenannten „Kelvaro“ (Farbcode Grün und Grau). Zusätzlich werden die Physiotherapeuten noch unter einer Marke zusammengefasst, dem sogenannten „Tesmunda“ (Farbcode Blau und Grün).
Kelvaro und Tesmunda haben jeweils eigene Internetseiten, Flyer und auch Visitenkarten.
Da jedoch beide Marken am selben Standort tätig sind, sollen auf diversen Plakaten (die im Umfeld der Ordination hängen werden) und den Schildern an der Türe auch beide Marken gemeinsam präsentiert werden.
Logos inkl. Farbrichtlinien wurden bereits gestaltet. Als Designvorlage dient ebenso ein allgemeiner Flyer über „Kelvaro“ (s. Anhang).
Im Anhang an das Briefing finden Sie alle relevanten Dateien wie Logos, Farbcodes, Fotos etc., die Sie zur Gestaltung der Werbemittel benötigen. Die grafische Umsetzung, Gliederung etc. überlassen wir Ihnen und freuen uns auf übersichtliche Vorschläge. Es wäre schön, wenn sich die Farbcodes der jeweiligen Marken auch in den Werbemitteln widerspiegeln. Wichtig ist uns, dass die Werbemittel klar und gut strukturiert gestaltet sind und nicht überladen wirken.
Hier finden Sie all mögliche Logo-Dateien, den bestehenden Flyer, die Farbwerte ,...
https://filedrop-example.net/t-Xq4bnLzPae
Farbregeln:
Wenn im Werbemittel nur ein Logo vorkommt, dann ist die Farbregel wie folgt:
Farbcode Kelvaro: Grün und Grau
Farbcode Tesmunda: Blau und Grün
Wenn im Werbemittel beide Logos vorkommen, dann ist die Farbregel wie folgt:
Farbcode Kelvaro: bleibt Grün und Grau
Farbcode Tesmunda: wird geändert in Blau und Grau
Viele der Werbemittel werden bei plakatfix.at produziert. Wenn Sie den jeweiligen Link beim Punkt „Datenaufbereitung“ anklicken, können Sie falls nötig auch direkt Formatvorlagen in diver..
Aufgabenstellung
Dieser Auftrag umfasst die Gestaltung von vier Plakaten in div. Größen mit identem Inhalt.
Bitte gestallten Sie zu Beginn nur die Größe 4000x1500cm
Sobald sich das Design in die richtige Richtung entwickelt, können dann auch die anderen Größen angelegt werden.
--> Bei zufriedenstellender Arbeit stehen eine Reihe von Folgeaufträgen an. (Siehe unten)
Plakate (4 Stück)
1. Plakat
Größe: 4000x1500cm
Info: Hängt zur Bewerbung der Praxis im Außenbereich an diversen Standorten in den umliegenden Orten, auf einer Höhe von ca. 3 Metern und soll vor allem vorbeifahrende Autofahrer ansprechen.
Inhalt:
Die Logos Kelvaro und Tesmunda
Die Adresse: Lindenhofweg 17/3, 3187 Morvenau
E-Mailadressen office@kelvaro.net und office@tesmunda.at
Websites: www.kelvaro.net und www.tesmunda.at
Text: „Gemeinschaftspraxis für Orthopädie und Physiotherapie“
Fachbereiche/Schlagwörter: Unfallchirurgie, Sportmedizin, Rehabilitation, Sportphysiotherapie
Weitere optionale Schlagworte: Chiropraktik, Akupunktur, Prävention, Massagen
Datenaufbereitung:
Druckformat: 4060x1560mm
Sicherheitsabstand: 40mm
Abstand vom Ösenmittelpunkt zum Rand: 15mm
Abstand der Ösen zueinander: ca 500mm
Ösendurchmesser: 15mm
https://www.plakatfix.at/produkte/banner-transparente/transparente-planen-banner/
2. Plakat
Größe: 3000x1000mm
Inhalt/Info: identisch zu Plakat Nr. 1 4000x1500, nur das Format ist anders.
Druckformat: 3060x1060mm
3. Plakat
Größe: 4000x850mm
Info: Hängt auf der Fassade unseres Gebäudes und soll den Standort der Ordination klar kennzeichnen. Soll vorbeifahrende Autofahrer und Fußgänger auf die Ordinat..

```html
<!DOCTYPE html>
<html lang="de">
<head>
<meta charset="utf-8">
<title>Kelvaro &amp; Tesmunda – Banner</title>
<link href="https://fonts.googleapis.com/css2?family=Source+Sans+3:wght@400;700&display=swap" rel="stylesheet">
<style>
  :root {
    --stage: #e6e6e6;
    --banner-bg: #f5f5f5;
    --banner-circle: #ebebeb;
    --brand-green: #72bf36;
    --brand-green-dark: #1f9a48;
    --brand-blue: #1a74c4;
    --text-grey: #6d6d6d;
    --white: #ffffff;
  }
  html, body {
    margin: 0;
    width: 1200px;
    height: 934px;
    overflow: hidden;
    background: var(--stage);
    font-family: "Source Sans 3", sans-serif;
  }
  .banner {
    position: absolute;
    left: 20px;
    top: 253px;
    width: 1160px;
    height: 426px;
    display: block;
  }
  .banner-bg { fill: var(--banner-bg); }
  .deco-circle { fill: var(--banner-circle); }
  .kicker { font-weight: 700; font-size: 33px; fill: var(--text-grey); letter-spacing: 0.5px; }
  .headline { font-weight: 700; font-size: 60px; fill: var(--brand-green); }
  .service { font-weight: 400; font-size: 35px; fill: var(--text-grey); }
  .bullet { fill: var(--brand-green); }
  .brand-kelvaro { font-weight: 700; font-size: 40px; fill: var(--brand-green); letter-spacing: 1px; }
  .brand-tesmunda { font-weight: 700; font-size: 40px; fill: var(--brand-blue); letter-spacing: 1px; }
  .dot-green { fill: var(--brand-green); }
  .dot-blue { fill: var(--brand-blue); }
  .accent-green { fill: var(--brand-green); }
  .web-cap { fill: var(--brand-blue); stroke: var(--white); stroke-width: 6; }
  .web-link { font-weight: 700; font-size: 25px; fill: var(--white); text-anchor: middle; }
  .address { font-weight: 400; font-size: 25px; fill: var(--text-grey); }
  .address-sep { fill: var(--brand-green); font-weight: 700; }
  .pin { fill: var(--brand-green); }
</style>
</head>
<body>
<svg class="banner" viewBox="0 0 1559 573" xmlns="http://www.w3.org/2000/svg">
  <defs>
    <clipPath id="banner-clip"><rect width="1559" height="573"/></clipPath>
    <linearGradient id="rule-gradient" x1="0" x2="1">
      <stop offset="0" stop-color="#1f9a48"/>
      <stop offset="1" stop-color="#72bf36"/>
    </linearGradient>
    <linearGradient id="photo-tones" x1="0" y1="0" x2="1" y2="1">
      <stop offset="0" stop-color="#d9d6cf"/>
      <stop offset="0.45" stop-color="#9aa5ad"/>
      <stop offset="0.75" stop-color="#6f8fae"/>
      <stop offset="1" stop-color="#c9ccc9"/>
    </linearGradient>
  </defs>

  <g clip-path="url(#banner-clip)">
    <rect class="banner-bg" width="1559" height="573"/>
    <circle class="deco-circle" cx="117" cy="210" r="230"/>
    <circle class="deco-circle" cx="617" cy="320" r="155"/>

    <!-- Headline block -->
    <text class="kicker" x="60" y="86">GEMEINSCHAFTSPRAXIS FÜR</text>
    <text class="headline" x="60" y="152">ORTHOPÄDIE</text>
    <text class="headline" x="60" y="217" textLength="614" lengthAdjust="spacingAndGlyphs">UND PHYSIOTHERAPIE</text>
    <rect x="60" y="236" width="615" height="8" fill="url(#rule-gradient)"/>

    <!-- Services -->
    <circle class="bullet" cx="67" cy="284" r="5"/>
    <text class="service" x="102" y="296">Unfallchirurgie</text>
    <circle class="bullet" cx="67" cy="326" r="5"/>
    <text class="service" x="102" y="338">Sportmedizin</text>
    <circle class="bullet" cx="372" cy="284" r="5"/>
    <text class="service" x="406" y="296">Rehabilitation</text>
    <circle class="bullet" cx="372" cy="326" r="5"/>
    <text class="service" x="406" y="338">Sportphysiotherapie</text>

    <!-- Brand names -->
    <circle class="dot-green" cx="262" cy="418" r="38"/>
    <text class="brand-kelvaro" x="60" y="498">KELVARO</text>
    <circle class="dot-blue" cx="600" cy="418" r="38"/>
    <text class="brand-tesmunda" x="380" y="498">TESMUNDA</text>

    <!-- Photo area -->
    <path class="accent-green" d="M905,0 Q790,250 1020,402 L1240,300 L1240,0 Z"/>
    <circle class="accent-green" cx="1240" cy="103" r="358"/>
    <g role="img" aria-label="Fotocollage: Arzt erklärt Anatomie-Tafel, Physiotherapeut behandelt Schulter eines älteren Patienten, Trainer und Sportler bei Übungen">
      <circle cx="1240" cy="95" r="352" fill="url(#photo-tones)" stroke="var(--white)" stroke-width="6"/>
    </g>

    <!-- Web addresses -->
    <path class="web-cap" d="M1118,-6 L1565,-6 L1565,92 Q1430,160 1300,152 Q1170,135 1118,-6 Z"/>
    <text class="web-link" x="1374" y="73">www.kelvaro.net</text>
    <text class="web-link" x="1374" y="103">www.tesmunda.at</text>

    <!-- Address -->
    <path class="pin" d="M959,488 a10,10 0 0 1 10,10 c0,8 -10,18 -10,18 c0,0 -10,-10 -10,-18 a10,10 0 0 1 10,-10 Z M959,494 a4,4 0 1 0 0.01,0 Z" fill-rule="evenodd"/>
    <text class="address" x="982" y="511">Lindenhofweg 17 <tspan class="address-sep">|</tspan> TOP 3 <tspan class="address-sep">|</tspan> 3187 Morvenau</text>
  </g>
</svg>
</body>
</html>
```